Glass window Vinyl

We are in need of window vinyls for the building shown in the photos. The current vinyls will come down, and we will install the new signage created by this process. We need to advertise:

"Hartwell's Landing Pop Up Market"

Then, below that, it should say for rental inquiries call : 717.555.0193 with our logo which is attached along with our colors and brand guidelines. You may add more color to the Hartwells landing pop up market signage if appropriate. It should be large enough to be easily read from the road by those passing by.

```html
<!DOCTYPE html>
<html lang="en">
<head>
<meta charset="utf-8">
<title>Hartwell's Landing Pop Up Market – Window Vinyls</title>
<link rel="stylesheet" href="https://fonts.googleapis.com/css2?family=Lato:wght@300;400&family=Marcellus&family=Montserrat:wght@400;500;700&display=swap">
<style>
  :root {
    --teal: #133f4d;
    --gold: #b8a06a;
    --white: #ffffff;
    --page: #ffffff;
  }
  * { margin: 0; padding: 0; box-sizing: border-box; }
  html, body { width: 1200px; height: 690px; overflow: hidden; background: var(--page); }
  .canvas { position: relative; width: 1200px; height: 690px; }

  .vinyl {
    position: absolute;
    top: 74px;
    width: 470px;
    height: 539px;
    background: var(--teal);
    box-shadow: 6px 8px 14px rgba(0,0,0,0.28);
  }
  .vinyl--market { left: 78px; }
  .vinyl--photo { left: 649px; }

  .vinyl__frame {
    position: absolute;
    inset: 11px;
    border: 2px solid var(--gold);
  }
  .vinyl__rules { position: absolute; inset: 0; pointer-events: none; }

  .brand { position: absolute; left: 0; right: 0; text-align: center; }
  .brand__mark {
    display: block;
    margin: 0 auto;
    border: 1.5px solid var(--gold);
  }
  .brand__name {
    font-family: "Marcellus", serif;
    color: var(--white);
    letter-spacing: 0.2em;
    line-height: 1;
  }
  .brand__sub {
    font-family: "Marcellus", serif;
    color: var(--white);
    letter-spacing: 0.42em;
    line-height: 1;
  }

  .vinyl--market .brand { top: 52px; }
  .vinyl--market .brand__mark { width: 14px; height: 14px; margin-bottom: 22px; }
  .vinyl--market .brand__name { font-size: 23px; padding-left: 0.2em; }
  .vinyl--market .brand__sub { font-size: 11px; margin-top: 20px; padding-left: 0.42em; }

  .vinyl--photo .brand { top: 38px; }
  .vinyl--photo .brand__mark { width: 11px; height: 11px; margin-bottom: 16px; }
  .vinyl--photo .brand__name { font-size: 18px; padding-left: 0.2em; }
  .vinyl--photo .brand__sub { font-size: 9px; margin-top: 13px; padding-left: 0.42em; }

  .market-band {
    position: absolute;
    left: 11px; right: 11px;
    top: 171px;
    height: 182px;
    background: var(--gold);
    text-align: center;
    font-family: "Lato", sans-serif;
  }
  .market-band__title {
    display: block;
    color: var(--white);
    font-weight: 400;
    font-size: 47px;
    line-height: 52px;
    letter-spacing: 0.01em;
  }
  .market-band__title:first-child { margin-top: 18px; }
  .market-band__sub {
    display: block;
    color: var(--teal);
    font-weight: 300;
    font-size: 35px;
    line-height: 44px;
    margin-top: 2px;
  }

  .inquiries {
    position: absolute;
    left: 0; right: 0;
    top: 384px;
    text-align: center;
    font-family: "Montserrat", sans-serif;
    font-weight: 700;
    font-size: 23px;
    color: var(--gold);
    letter-spacing: 0.01em;
  }

  .contact {
    position: absolute;
    left: 63px;
    top: 432px;
    display: flex;
    align-items: center;
    gap: 14px;
  }
  .contact__call {
    display: inline-block;
    width: 73px; height: 32px;
    border-radius: 5px;
    background: var(--gold);
    color: var(--teal);
    font-family: "Montserrat", sans-serif;
    font-weight: 700;
    font-size: 16px;
    line-height: 32px;
    text-align: center;
  }
  .contact__phone {
    font-family: "Marcellus", serif;
    color: var(--white);
    font-size: 45px;
    line-height: 46px;
    letter-spacing: 0.01em;
  }

  .web {
    position: absolute;
    left: 0; right: 0;
    text-align: center;
    font-family: "Montserrat", sans-serif;
    font-weight: 400;
    font-size: 13px;
    color: var(--gold);
  }
  .vinyl--market .web { top: 492px; }
  .vinyl--photo .web { top: 489px; }

  .photo-slot {
    position: absolute;
    left: 12px; right: 12px;
    top: 134px;
    height: 272px;
    background: var(--gold);
    padding: 4px 3px;
  }
  .photo-slot__fill {
    width: 100%; height: 100%;
    background: linear-gradient(180deg, #d9d9d6 0%, #bdbcb6 55%, #8d8a84 75%, #3a2c25 100%);
  }
</style>
</head>
<body>
<main class="canvas">

  <section class="vinyl vinyl--market">
    <div class="vinyl__frame"></div>
    <svg class="vinyl__rules" width="470" height="539" viewBox="0 0 470 539" aria-hidden="true">
      <g stroke="#b8a06a" stroke-width="1">
        <line x1="27" y1="79" x2="27" y2="171"/>
        <line x1="40" y1="116" x2="40" y2="171"/>
        <line x1="430" y1="30" x2="430" y2="171"/>
        <line x1="443" y1="30" x2="443" y2="171"/>
        <line x1="27" y1="353" x2="27" y2="509"/>
        <line x1="40" y1="353" x2="40" y2="509"/>
        <line x1="430" y1="353" x2="430" y2="422"/>
        <line x1="443" y1="353" x2="443" y2="460"/>
      </g>
    </svg>

    <div class="brand">
      <span class="brand__mark"></span>
      <p class="brand__name">JUNIPER ROW</p>
      <p class="brand__sub">PROPERTIES</p>
    </div>

    <div class="market-band">
      <span class="market-band__title">HARTWELL'S</span>
      <span class="market-band__title">LANDING</span>
      <span class="market-band__sub">POP UP MARKET</span>
    </div>

    <p class="inquiries">FOR RENTAL INQUIRIES</p>

    <div class="contact">
      <span class="contact__call">CALL</span>
      <span class="contact__phone">717.555.0193</span>
    </div>

    <p class="web">www.juniperrowproperties.com</p>
  </section>

  <section class="vinyl vinyl--photo">
    <div class="vinyl__frame"></div>
    <svg class="vinyl__rules" width="470" height="539" viewBox="0 0 470 539" aria-hidden="true">
      <g stroke="#b8a06a" stroke-width="1">
        <line x1="27" y1="33" x2="27" y2="134"/>
        <line x1="40" y1="76" x2="40" y2="134"/>
        <line x1="429" y1="33" x2="429" y2="134"/>
        <line x1="443" y1="33" x2="443" y2="134"/>
        <line x1="27" y1="406" x2="27" y2="506"/>
        <line x1="40" y1="406" x2="40" y2="506"/>
        <line x1="429" y1="406" x2="429" y2="430"/>
        <line x1="443" y1="406" x2="443" y2="506"/>
      </g>
    </svg>

    <div class="brand">
      <span class="brand__mark"></span>
      <p class="brand__name">JUNIPER ROW</p>
      <p class="brand__sub">PROPERTIES</p>
    </div>

    <div class="photo-slot">
      <div class="photo-slot__fill" role="img" aria-label="Photo of a renovated rental apartment kitchen with grey cabinets, white subway tile, stainless fridge and dark wood floor"></div>
    </div>

    <div class="contact">
      <span class="contact__call">CALL</span>
      <span class="contact__phone">717.555.0193</span>
    </div>

    <p class="web">www.juniperrowproperties.com</p>
  </section>

</main>
</body>
</html>
```